Home Staging Company needs business card design

We're a home staging company called Brightly Settled Home Staging. We would like a business card design that includes aqua and gray. Our current logo of house within chair is fine but I find we almost always use the logo in one color. I'll upload images of front and back of our current card and our logo. Note that we have dropped "Solutions" from our company name and don't want to include it on the card.

Target Market(s)

Realtors and homeowners - people interested in selling their homes

Contact Information for Business Card

Marisol Vantrease
Brightly Settled Home Staging
612-348-9071
www.brightlysettled.example
marisol@brightlysettled.example

Font styles to use
Serif
Script

Requirements
Must have
• My logo and contact details
• UPDATE***
• I forgot to say that the company name should be included on the front of the card somehow.

```html
<!DOCTYPE html>
<html lang="en">
<head>
<meta charset="utf-8">
<title>Brightly Settled Home Staging – Business Card</title>
<link rel="stylesheet" href="https://fonts.googleapis.com/css2?family=Playfair+Display:wght@400&family=Roboto+Condensed:wght@400&family=Questrial&display=swap">
<style>
  :root {
    --backdrop: #a8a8a8;
    --charcoal: #383c3f;
    --charcoal-deep: #2f3336;
    --paper: #f1f1f1;
    --aqua: #4aacb6;
    --ink: #3a3d40;
    --ink-soft: #55595c;
    --white: #f4f4f4;
  }
  * { margin: 0; padding: 0; box-sizing: border-box; }
  html, body { width: 1200px; height: 576px; overflow: hidden; background: var(--backdrop); }
  .canvas { position: relative; width: 1200px; height: 576px; }

  .card {
    position: absolute;
    top: 138px;
    width: 484px;
    height: 294px;
    border-radius: 12px;
    overflow: hidden;
  }

  /* Front */
  .card-front { left: 82px; background: var(--charcoal); }
  .card-front .company-name {
    position: absolute; left: 0; right: 0; top: 112px;
    text-align: center;
    font-family: "Playfair Display", serif; font-weight: 400;
    color: var(--white);
  }
  .card-front .company-name .line-main { display: block; font-size: 40px; line-height: 1; }
  .card-front .company-name .line-sub { display: block; font-size: 16px; letter-spacing: 9px; margin-top: 8px; }
  .card-front .web {
    position: absolute; left: 0; right: 0; bottom: 13px;
    text-align: center;
    font-family: "Questrial", sans-serif; font-size: 13px;
    color: var(--aqua);
  }

  /* Back */
  .card-back { left: 602px; background: var(--paper); }
  .brand-block {
    position: absolute; left: 36px; top: 58px; width: 190px;
    text-align: center;
    font-family: "Playfair Display", serif; font-weight: 400;
    color: var(--ink);
  }
  .brand-block .brand-dot {
    display: block; width: 64px; height: 64px; margin: 0 auto 18px;
    border-radius: 50%; background: var(--aqua);
  }
  .brand-block .line-main { display: block; font-size: 24px; line-height: 1; }
  .brand-block .line-sub { display: block; font-size: 10px; letter-spacing: 5px; margin-top: 6px; }

  .person { position: absolute; left: 256px; top: 82px; }
  .person .name {
    font-family: "Roboto Condensed", sans-serif; font-size: 20px;
    color: var(--ink);
  }
  .person .role {
    font-family: "Questrial", sans-serif; font-size: 11px;
    color: var(--ink-soft); margin-top: 4px;
  }
  .contacts { position: absolute; left: 256px; top: 136px; list-style: none; }
  .contacts li {
    display: flex; align-items: center; gap: 11px;
    height: 17.5px;
    font-family: "Questrial", sans-serif; font-size: 12px;
    color: var(--ink);
  }
  .contacts svg { width: 10px; height: 10px; fill: var(--aqua); flex: none; }

  .base-strip { position: absolute; left: 0; right: 0; bottom: 0; height: 10px; background: var(--charcoal-deep); }
  .cta-tab {
    position: absolute; right: 0; bottom: 0; width: 266px; height: 35px;
    background: var(--aqua);
    clip-path: polygon(12px 0, 100% 0, 100% 100%, 0 100%);
    border-top-left-radius: 6px;
    display: flex; align-items: center; justify-content: center;
    font-family: "Questrial", sans-serif; font-size: 12px;
    color: var(--white);
  }
</style>
</head>
<body>
<main class="canvas">

  <section class="card card-front" aria-label="Card front">
    <h1 class="company-name">
      <span class="line-main">Brightly Settled</span>
      <span class="line-sub">HOME STAGING</span>
    </h1>
    <p class="web">www.brightlysettled.example</p>
  </section>

  <section class="card card-back" aria-label="Card back">
    <div class="brand-block">
      <span class="brand-dot"></span>
      <span class="line-main">Brightly Settled</span>
      <span class="line-sub">HOME STAGING</span>
    </div>

    <div class="person">
      <p class="name">Marisol Vantrease</p>
      <p class="role">Managing Director</p>
    </div>

    <ul class="contacts">
      <li>
        <svg viewBox="0 0 10 10" aria-hidden="true"><path d="M1 3.5C1 2 2.5 1 5 1s4 1 4 2.5L7.5 4 7 3H3L2.5 4zM2.5 4.5h5L9 9H1z"/></svg>
        612-348-9071
      </li>
      <li>
        <svg viewBox="0 0 10 10" aria-hidden="true"><path d="M5 0.5a4.5 4.5 0 1 0 0 9 4.5 4.5 0 0 0 0-9zm0 1c.6.6 1 1.6 1.1 2.8H3.9C4 3.1 4.4 2.1 5 1.5zM1.6 4.3h1.3c.1 1.2.4 2.2.9 3A3.5 3.5 0 0 1 1.6 5.7zm0-.1zm6.8 0v1.4a3.5 3.5 0 0 1-2.2 1.6c.5-.8.8-1.8.9-3zM3.9 5.7h2.2C6 6.9 5.6 7.9 5 8.5c-.6-.6-1-1.6-1.1-2.8z"/></svg>
        www.brightlysettled.example
      </li>
      <li>
        <svg viewBox="0 0 10 10" aria-hidden="true"><path d="M0.5 2h9v6h-9zM1.3 2.6 5 5.6l3.7-3z" fill-rule="evenodd"/></svg>
        marisol@brightlysettled.example
      </li>
    </ul>

    <div class="base-strip"></div>
    <p class="cta-tab">Schedule a consultation today!</p>
  </section>

</main>
</body>
</html>
```